Carpet cleaning company wants business card

Need an exciting new fresh design for business cards for my carpet cleaning /pest control business
www.tidewellhomecare.com.au
Can design include a lined section for quoting or information? Thanks !

```html
<!DOCTYPE html>
<html lang="en">
<head>
<meta charset="utf-8">
<title>Tidewell Home Care – Business Card</title>
<link href="https://fonts.googleapis.com/css2?family=Josefin+Sans:wght@400;600;700&display=swap" rel="stylesheet">
<style>
  :root{
    --bg:#e4e5e7;
    --paper:#ffffff;
    --red:#ee3a3a;
    --blue:#1458ac;
    --ink:#555a60;
    --rule:#f3a3a3;
  }
  *{box-sizing:border-box;margin:0;padding:0}
  html,body{width:1200px;height:800px;overflow:hidden;background:var(--bg)}
  body{font-family:"Josefin Sans",Arial,sans-serif;color:var(--ink);position:relative}
  .card{position:absolute;top:235px;width:540px;height:330px;background:var(--paper);
        box-shadow:0 6px 18px rgba(0,0,0,.12);overflow:hidden}
  .card--back{left:40px}
  .card--front{left:620px}
  .wordmark{font-weight:700;font-size:30px;line-height:1;color:var(--red);display:flex;align-items:center;gap:10px;white-space:nowrap}
  .wordmark__dot{width:14px;height:14px;background:var(--blue);flex:none}

  /* front */
  .card--front .wordmark{position:absolute;left:36px;top:44px}
  .owners{position:absolute;left:36px;top:120px;font-size:17px;color:var(--red)}
  .owners span{color:var(--ink);font-size:13px}
  .contact{position:absolute;left:36px;right:30px;top:160px;display:flex;gap:12px;font-size:11.5px;line-height:20px;white-space:nowrap}
  .contact__group{display:flex;flex-direction:column}
  .contact__group + .contact__group{border-left:1px solid var(--blue);padding-left:12px}
  .contact__row{display:flex;align-items:center;gap:7px}
  .contact__row svg{width:11px;height:11px;fill:var(--blue);flex:none}
  .divider{position:absolute;left:36px;right:36px;top:226px;height:1px;background:var(--rule)}
  .hours-band{position:absolute;left:0;right:0;bottom:0;height:72px;background:var(--blue);color:#fff;
              font-size:15px;display:flex;align-items:center;padding-left:36px}

  /* back */
  .back__title{position:absolute;left:36px;top:30px;font-size:15px;color:var(--red);font-weight:600}
  .card--back .wordmark{position:absolute;right:30px;top:26px;font-size:22px}
  .services{position:absolute;left:36px;right:30px;top:62px;font-size:11.5px;line-height:17px}
  .quote__label{position:absolute;left:36px;top:150px;font-size:15px;color:var(--blue);font-weight:600}
  .quote__lines{position:absolute;left:36px;right:36px;top:176px}
  .quote__line{height:26px;border-bottom:2px dotted var(--blue)}
  .quote__line:first-child{margin-left:110px;margin-top:-26px}
  .accent-band{position:absolute;left:0;right:0;bottom:0;height:56px;background:var(--red)}
</style>
</head>
<body>

<section class="card card--back" aria-label="Card back">
  <h2 class="back__title">TIDEWELL HOME CARE</h2>
  <div class="wordmark"><span class="wordmark__dot"></span>Tidewell Home Care</div>
  <p class="services">
    Residential Carpet / Commercial Carpet<br>
    Rental Bond Carpet Cleaning &amp; Pest Control<br>
    Pest Control Cairns / Furniture and Upholstery Cleaning Cairns<br>
    Tile and Grout Cleaning Services / Mats and Rug Cleaning Cairns / Water Extraction
  </p>
  <h3 class="quote__label">For Quoting</h3>
  <div class="quote__lines">
    <div class="quote__line"></div>
    <div class="quote__line"></div>
    <div class="quote__line"></div>
    <div class="quote__line"></div>
  </div>
  <div class="accent-band"></div>
</section>

<section class="card card--front" aria-label="Card front">
  <div class="wordmark"><span class="wordmark__dot"></span>Tidewell Home Care</div>
  <p class="owners">Maren &amp; Theo | <span>Owners</span></p>
  <div class="contact">
    <div class="contact__group">
      <div class="contact__row"><svg viewBox="0 0 12 12"><rect x="3" y="0" width="6" height="12" rx="1"/></svg>0412 555 017</div>
      <div class="contact__row"><svg viewBox="0 0 12 12"><path d="M2 1l3 0 1 3-2 1c1 2 2 3 3 3l1-2 3 1 0 3c-6 0-9-3-9-9z"/></svg>07 5550 1234</div>
    </div>
    <div class="contact__group">
      <div class="contact__row"><svg viewBox="0 0 12 12"><path d="M0 2h12v8H0z M0 2l6 5 6-5" stroke="#fff" stroke-width=".8"/></svg>admin@tidewellhomecare.com.au</div>
      <div class="contact__row"><svg viewBox="0 0 12 12"><circle cx="6" cy="6" r="6"/></svg>www.tidewellhomecare.com.au</div>
    </div>
    <div class="contact__group">
      <div>3/22 Harlow Court</div>
      <div>Brookvale 4210</div>
    </div>
  </div>
  <div class="divider"></div>
  <div class="hours-band">Opening Hours: Mon to Fri – 8:00am to 6:00pm</div>
</section>

</body>
</html>
```